We need motivational posters designed to be used in classrooms at a truck driving school. The purpose of the posters is to motivate the students.

I want the the quotes to be the main focal point of emphasis and our logo on the bottom of the poster for branding purposes.

I would like the images to be related to the trucking industry

Below are the quotes for the posters

Poster 1
"Start where you are. Use what you have. Do what you can."
-Delmar Quisby-

Poster 2
"The secret of getting ahead is getting started"
-Owen Farrow-

Poster 3
"Most effective way to do it, is to do it."
-Rosalind Pemberly-

Poster 4
"Set your goals big, and don't stop till you get there."
-Cy Whitlock-

Poster 5
"If you are not willing to learn, no one can help you. If you are determined to learn, no one can stop you."
-Unknown-

Poster 6
"The will to succeed is important, but what's more important is the will to prepare."
-Dougie Hallam-

THESE POSTERS SHOULD BE DESIGNED AS 18X24
LANDSCAPE AND PORTRAIT ORIENTATION

Industry/Entity Type

School

```html
<!DOCTYPE html>
<html lang="en">
<head>
<meta charset="UTF-8">
<title>Poster 6 – The Will to Prepare</title>
<link href="https://fonts.googleapis.com/css2?family=Libre+Bodoni:wght@700&family=Arimo:wght@400;700&display=swap" rel="stylesheet">
<style>
  :root {
    --sky-top: #d3dadd;
    --sky-cloud: #c4cacd;
    --sky-low: #d9dee0;
    --horizon: #e4e7e8;
    --hills: #6f6a66;
    --land: #8b8272;
    --road-far: #5a5f63;
    --road-mid: #4a4f53;
    --road-near: #3a3f42;
    --ink: #111314;
    --band: #ffffff;
    --brand-gold: #e2a919;
    --brand-dark: #1c1d1f;
  }
  * { margin: 0; padding: 0; box-sizing: border-box; }
  html, body { width: 900px; height: 1200px; overflow: hidden; background: var(--band); }
  .poster { position: relative; width: 900px; height: 1200px; }
  .scene-photo {
    position: absolute; left: 0; top: 0; width: 900px; height: 1100px;
    background: linear-gradient(180deg,
      var(--sky-top) 0%,
      var(--sky-low) 22%,
      var(--sky-cloud) 38%,
      var(--sky-low) 47%,
      var(--horizon) 52%,
      var(--hills) 54.5%,
      var(--land) 58%,
      var(--land) 62%,
      var(--road-far) 67%,
      var(--road-mid) 80%,
      var(--road-near) 100%);
  }
  .quote {
    position: absolute; left: 40px; top: 72px; width: 850px;
    font-family: "Libre Bodoni", "Bodoni Moda", serif;
    font-weight: 700; font-size: 51px; line-height: 59px;
    word-spacing: 5px;
    color: var(--ink);
  }
  .quote-author {
    position: absolute; left: 40px; top: 281px;
    font-family: "Arimo", Arial, sans-serif;
    font-size: 26px; letter-spacing: 0.3px;
    color: var(--ink); text-transform: uppercase;
  }
  .brand-band {
    position: absolute; left: 0; top: 1100px; width: 900px; height: 100px;
    background: var(--band);
    display: flex; align-items: center; padding-left: 40px; gap: 10px;
  }
  .brand-mark { width: 58px; height: 58px; border-radius: 50%; background: var(--brand-dark); flex: none; }
  .brand-name {
    font-family: "Arimo", Arial, sans-serif; font-weight: 700;
    font-size: 18px; line-height: 20px; color: var(--brand-gold);
    text-transform: uppercase; width: 180px;
  }
</style>
</head>
<body>
  <main class="poster">
    <div class="scene-photo" role="img" aria-label="Empty two-lane highway stretching through a barren valley toward snowy hills under an overcast sky"></div>
    <blockquote class="quote">The will to succeed is important,<br>but what's more important is<br>the will to prepare.</blockquote>
    <p class="quote-author">Dougie Hallam</p>
    <footer class="brand-band">
      <span class="brand-mark"></span>
      <span class="brand-name">Summit Haul Driving School</span>
    </footer>
  </main>
</body>
</html>
```